Starter Nest to Forever Manor - House

This will be converted to vinyl signage for the windows in front of my building dimensions are approximately 9 feet long by six feet high
I would like a creative design showing three homes in One
the homes should progress from
a typical first home
to a mid-level upgrade home,
then a fabulous dream home
I like the concept in the picture with the homes growing in size but i don't like the plane little homes

I would like this designed in photoshop

Target Market(s)

24-50 age renage

Industry/Entity Type

Real Estate Agent

Logo Text

Starter Nest to Forever Manor

Font styles to use
Sans Serif

Requirements
Must have
• color scheme to match the included logo
• I am searching for homes that are the same color
• grey, white or maroon,
• or perhaps the same build material (stone or brick) and still show the same progression from small 1st home to final luxury home

```html
<!DOCTYPE html>
<html lang="en">
<head>
<meta charset="utf-8">
<title>Starter Nest to Forever Manor</title>
<link rel="stylesheet" href="https://fonts.googleapis.com/css2?family=Montserrat:wght@700;800&display=swap">
<style>
  :root {
    --paper: #ffffff;
    --ink: #111111;
    --maroon: #8e0f12;
    --chart-red: #d91f25;
    --band-red: #a3161b;
    --blush: #fbe9ec;
    --brand-slate: #3b4450;
    --house-cream: #e4dccb;
    --house-stone: #cfc6b4;
  }
  * { margin: 0; padding: 0; box-sizing: border-box; }
  html, body { width: 1200px; height: 800px; overflow: hidden; background: var(--paper); }
  .sign {
    position: relative;
    width: 1200px;
    height: 800px;
    background: var(--paper);
    overflow: hidden;
    font-family: "Montserrat", Arial, sans-serif;
  }
  .chart { position: absolute; inset: 0; width: 1200px; height: 800px; }
  .headline { font-weight: 800; font-variant: small-caps; line-height: 1; }
  .headline__line { position: absolute; left: 72px; white-space: nowrap; }
  .headline__lead { top: 66px; color: var(--ink); font-size: 64px; }
  .headline__goal { top: 150px; color: var(--maroon); font-size: 126px; }
  .headline__end { top: 280px; color: var(--maroon); font-size: 106px; }
  .brand {
    position: absolute;
    left: 770px; top: 104px;
    display: flex; align-items: center; gap: 12px;
  }
  .brand__dot { width: 24px; height: 24px; border-radius: 50%; background: var(--brand-slate); }
  .brand__name { color: var(--brand-slate); font-size: 30px; font-weight: 800; }
  .house { position: absolute; border-radius: 4px; }
  .house--starter {
    left: 36px; top: 628px; width: 296px; height: 124px;
    background: linear-gradient(180deg, #f1ecdf 0%, var(--house-cream) 55%, #c9d9b0 100%);
  }
  .house--upgrade {
    left: 341px; top: 470px; width: 330px; height: 244px;
    background: linear-gradient(180deg, #ece7dd 0%, var(--house-stone) 50%, #c6a39c 100%);
  }
  .house--manor {
    left: 664px; top: 324px; width: 536px; height: 336px;
    background: linear-gradient(180deg, #ede9e0 0%, var(--house-stone) 45%, #b9c7bf 100%);
  }
  .web { position: absolute; left: 680px; top: 710px; width: 520px; height: 47px; }
  .web__band { position: absolute; inset: 0; }
  .web__text {
    position: absolute; left: 58px; top: 0; height: 47px; line-height: 47px;
    color: #ffffff; font-size: 22px; font-weight: 700; letter-spacing: 0.5px;
    text-transform: uppercase;
  }
</style>
</head>
<body>
<main class="sign">
  <svg class="chart" viewBox="0 0 1200 800" aria-hidden="true">
    <polygon points="0,270 150,170 230,230 420,150 470,180 360,260 210,300 0,330" fill="var(--blush)" opacity="0.7"/>
    <polyline points="0,634 200,493 238,568 510,360 562,447 820,263 853,343 1200,127"
              fill="none" stroke="var(--chart-red)" stroke-width="17" stroke-linejoin="miter"/>
  </svg>

  <h1 class="headline">
    <span class="headline__line headline__lead">Starter Nest to</span>
    <span class="headline__line headline__goal">Forever</span>
    <span class="headline__line headline__end">Manor</span>
  </h1>

  <div class="brand">
    <span class="brand__dot"></span>
    <span class="brand__name">Hearthway Homes</span>
  </div>

  <div class="house house--starter" role="img" aria-label="Illustration of a small single-storey starter home with trees"></div>
  <div class="house house--upgrade" role="img" aria-label="Illustration of a two-storey mid-level upgrade home with garage and trees"></div>
  <div class="house house--manor" role="img" aria-label="Illustration of a large luxury dream home with gables, green roof and trees"></div>

  <div class="web">
    <svg class="web__band" width="520" height="47" viewBox="0 0 520 47" aria-hidden="true">
      <polygon points="22,0 520,0 520,47 0,47" fill="var(--band-red)"/>
    </svg>
    <span class="web__text">www.hearthwayhomes.com</span>
  </div>
</main>
</body>
</html>
```